Website for a web design agency

We are a website and marketing agency. We do website design, development, and well as Brindle and Quorvia advertising and analytics. We ourselves need a new website for our own brand. We are working on some designs in-house with our own designers, but we also wanted to see what outside designers would come up with.
We are starting off with the homepage, and here is the breakdown of the sections:
https://files.brindlework.example/sheet/d/7kqTr2VnPLwXeHsaMcY4oBfJzuGNtKdWiEh3Rx9pLmQb/view?mode=share
This doc also has many links to sites we have done, which you can take screenshots of for the portfolio section.
In terms of the "look" I am going for, I want to look high-end and very beautiful designs. I found this website that I like a lot that you can use some of the elements of, just as a starting point:
http://velmarkstudio.example/layouts/pixelbarn/html/ostrevo/index.html and here is another design option they have http://velmarkstudio.example/layouts/pixelbarn/html/ostrevo/index-4.html
I'm also uploading my logo. The logo matches the gold and black look from these websites, but I would be open to switching to another color scheme if needed.
This is the link to my very old website, which you can use for some of the dummy text, and a pic of myself. I will be taking more pics of myself:
https://theplumtreeandwillowgroup.example/
We need a homepage and a portfolio page right now, but if you are the winner, we will be hiring you to make additional pages.
Updates
More designs continue to come in even today, and I want to make sure no other designers are still submitting designs.
Target Market(s)
medium and large businesses owners, and non-profits
Number of Pages Required
1 page

```html
<!DOCTYPE html>
<html lang="en">
<head>
<meta charset="utf-8">
<title>Kestran Strategies — Homepage</title>
<link rel="stylesheet" href="https://fonts.googleapis.com/css2?family=Playfair+Display:wght@400;700&family=Roboto:wght@300;400;500;700&display=swap">
<style>
:root{
  --gold:#f0b22b;
  --gold-deep:#c99628;
  --ink:#1f1f1f;
  --ink-2:#262626;
  --slate:#3a3a37;
  --nav:#2b2b2b;
  --paper:#d7d7d7;
  --white:#ffffff;
  --muted:#b9b9b9;
  --board:#bdbdbd;
}
*{box-sizing:border-box;margin:0;padding:0}
html,body{width:1200px;height:1193px;overflow:hidden}
body{background:linear-gradient(180deg,#a8a8a8,#d9d9d9);font-family:'Roboto',sans-serif;color:var(--white);position:relative}
.abs{position:absolute}
.serif{font-family:'Playfair Display',serif}
.brand{color:var(--gold);font-family:'Roboto',sans-serif;font-weight:700;line-height:1;letter-spacing:.04em}
.brand small{display:block;font-size:.45em;letter-spacing:.32em;margin-top:2px}
.btn{background:var(--gold);color:var(--white);font-weight:700;display:flex;align-items:center;justify-content:center;letter-spacing:.12em;text-transform:uppercase}
.shot{background:linear-gradient(135deg,#3d4656,#1b2230)}

/* ---------- compact page ---------- */
.mini{left:89px;top:25px;width:292px;height:1133px;overflow:hidden;background:var(--slate)}
.mini .hero{left:0;top:0;width:292px;height:184px;background:linear-gradient(120deg,#2d2d2d,#4a4a48 60%,#3a3a38)}
.mini .navbar{left:0;top:0;width:292px;height:37px;background:var(--nav)}
.mini .navlinks{left:88px;top:16px;display:flex;gap:11px;font-size:4.3px;font-weight:700}
.mini h1{left:24px;top:48px;font-size:22px;line-height:27px;font-weight:400}
.mini .lead{left:24px;top:104px;font-size:6.6px;line-height:10.5px;font-weight:300}
.mini .hero .btn{left:24px;top:148px;width:81px;height:14px;font-size:3.8px}
.mini .video{left:146px;top:51px;width:119px;height:98px}
.mini .services{left:0;top:184px;width:292px;height:234px;background:var(--ink-2)}
.mini .kicker{font-size:6.5px;font-weight:300}
.mini .svc-title{font-size:13px}
.card{position:absolute;display:flex;flex-direction:column}
.card .art{flex:1}
.card .label{background:var(--gold-deep);display:flex;align-items:center;justify-content:center;text-align:center;line-height:1.15}
.mini .card{width:50px;height:76px}
.mini .card .label{height:24px;font-size:4.8px}
.mini .portfolio{left:0;top:418px;width:292px;height:286px;background:var(--slate)}
.mini .sec-title{width:100%;text-align:center;font-size:13px}
.work{position:absolute;overflow:hidden}
.work .cap{position:absolute;left:0;right:0;bottom:0;background:rgba(40,40,40,.78)}
.mini .work{width:77px;height:50px}
.mini .work .cap{padding:2px 4px;font-size:4.5px;line-height:5.3px}
.mini .portfolio .btn{left:105px;top:254px;width:81px;height:14px;font-size:3.5px}
.mini .quote{left:0;top:704px;width:292px;height:81px;background:var(--ink-2)}
.mini .quote p{left:74px;top:27px;width:176px;font-size:4.6px;line-height:6.8px;color:var(--muted)}
.mini .team{left:0;top:785px;width:292px;height:143px;background:var(--slate)}
.member{position:absolute}
.mini .member .photo{position:absolute;left:0;top:0;width:32px;height:32px;background:linear-gradient(160deg,#6b6f78,#2f3238);outline:1.5px solid var(--gold);outline-offset:2px}
.mini .member h4{position:absolute;left:41px;top:5px;font-size:4.2px;font-weight:700;white-space:nowrap}
.mini .member p{position:absolute;left:41px;top:13px;width:92px;font-size:3.3px;line-height:4.6px;color:#d0d0d0}
.mini .contact{left:0;top:928px;width:142px;height:153px;background:var(--ink-2)}
.mini .form{left:142px;top:928px;width:150px;height:153px;background:var(--paper)}
.field-label{position:absolute;font-size:2.4px;color:#777}
.field{position:absolute;background:#f4f4f4;border:0.5px solid #c4c4c4}
.mini .footer{left:0;top:1081px;width:292px;height:52px;background:#2a2a2a}

/* ---------- full-size page ---------- */
.full{left:468px;top:25px;width:641px;height:1168px;overflow:hidden;background:var(--slate)}
.full .hero{left:0;top:0;width:641px;height:404px;background:linear-gradient(115deg,#262626 0%,#4b4b48 55%,#2f2f2e 100%)}
.full .navbar{left:0;top:20px;width:641px;height:61px;background:var(--nav)}
.full .navlinks{left:195px;top:45px;display:flex;font-size:9.6px;font-weight:700;letter-spacing:.02em}
.full .navlinks span{position:absolute;white-space:nowrap}
.full h1{left:51px;top:104px;font-size:50px;line-height:59px;font-weight:700}
.full .lead{left:52px;top:230px;font-size:15.5px;line-height:23.5px;font-weight:300}
.full .hero .btn{left:52px;top:324px;width:180px;height:34px;font-size:9px}
.full .video{left:321px;top:113px;width:262px;height:216px;border:1px solid #555}
.full .services{left:0;top:404px;width:641px;height:514px;background:var(--ink)}
.full .kicker{font-size:15.5px;font-weight:300}
.full .svc-title{font-size:32.5px}
.full .card{width:109px;height:166px}
.full .card .label{height:48px;font-size:10.8px}
.full .portfolio{left:0;top:918px;width:641px;height:250px;background:var(--slate)}
.full .sec-title{font-size:30px;width:100%;text-align:center}
.full .work{width:169px;height:112px}
.full .work .cap{padding:4px 8px;font-size:8px;line-height:9px}
.full .work .cap b{font-size:11px;font-weight:400;display:block;line-height:13px}
</style>
</head>
<body>

<!-- ================= compact homepage ================= -->
<div class="abs mini">

  <section class="abs hero">
    <div class="abs video shot" role="img" aria-label="Laptop with code editor on a desk, with a play button"></div>
    <svg class="abs" style="left:196px;top:91px" width="20" height="20" viewBox="0 0 20 20"><circle cx="10" cy="10" r="8.5" fill="none" stroke="rgba(255,255,255,.6)" stroke-width="1.2"/><path d="M8 6l6 4-6 4z" fill="rgba(255,255,255,.6)"/></svg>
    <div class="abs navbar"></div>
    <div class="abs brand" style="left:24px;top:16px;font-size:10px">KESTRAN<small>STRATEGIES</small></div>
    <nav class="abs navlinks"><span>Home</span><span>What We Do</span><span>Portfolio</span><span>Testimonials</span><span>Our Team</span><span>Contact</span></nav>
    <h1 class="abs serif">We Build<br>Value</h1>
    <p class="abs lead">Enterprise Level<br>Website Development<br>and Online Marketing</p>
    <div class="abs btn">See how we do it</div>
  </section>

  <section class="abs services">
    <svg class="abs" style="left:131px;top:14px" width="146" height="168"><path d="M2 8V2H142V164H113" fill="none" stroke="var(--gold)" stroke-width="3"/></svg>
    <div class="abs kicker" style="left:24px;top:20px">What we do</div>
    <div class="abs serif svc-title" style="left:24px;top:33px">These are the things we CRUSH</div>
    <div class="card" style="left:60px;top:53px"><div class="art" style="background:linear-gradient(160deg,#3b6fd0,#d9dde6)" role="img" aria-label="Website screenshots"></div><div class="label">Websites</div></div>
    <div class="card" style="left:112px;top:53px"><div class="art" style="background:linear-gradient(160deg,#6c9fd6,#e0c58a)" role="img" aria-label="Landing page screenshots"></div><div class="label">Landing Pages</div></div>
    <div class="card" style="left:171px;top:53px"><div class="art" style="background:linear-gradient(160deg,#4b2a1c,#a0552c)" role="img" aria-label="Donation page screenshot"></div><div class="label">Donation Pages</div></div>
    <div class="card" style="left:60px;top:140px"><div class="art" style="background:linear-gradient(160deg,#3a1f7a,#7a3fb5)" role="img" aria-label="Sales funnel illustration"></div><div class="label">PPC and Funnels</div></div>
    <div class="card" style="left:112px;top:140px"><div class="art" style="background:linear-gradient(160deg,#c9c23a,#3b3a6e)" role="img" aria-label="Video marketing laptop illustration"></div><div class="label">Video Marketing</div></div>
    <div class="card" style="left:171px;top:140px"><div class="art" style="background:linear-gradient(160deg,#5ec0bd,#3d8f8c)" role="img" aria-label="Analytics magnifier illustration"></div><div class="label">Analytics and<br>Optimization</div></div>
  </section>

  <section class="abs portfolio">
    <div class="abs serif sec-title" style="top:23px">Our Portfolio</div>
    <div class="work" style="left:24px;top:53px"><div class="shot" style="height:100%" role="img" aria-label="Production company website"></div><div class="cap">Marlow Productions<br>Lorem ipsum dolor sit amet, consectetur</div></div>
    <div class="work" style="left:104px;top:53px"><div style="height:100%;background:linear-gradient(135deg,#5d4a8c,#c9b7a8)" role="img" aria-label="Charity website"></div><div class="cap">Hearthside Care<br>Lorem ipsum dolor sit amet, consectetur</div></div>
    <div class="work" style="left:187px;top:53px"><div style="height:100%;background:linear-gradient(135deg,#2b3340,#7b8392)" role="img" aria-label="Fitness website"></div><div class="cap">Ferrit X<br>Lorem ipsum dolor sit amet, consectetur</div></div>
    <div class="work" style="left:24px;top:118px"><div style="height:100%;background:linear-gradient(135deg,#3a4a66,#8a6a4a)" role="img" aria-label="Construction website"></div><div class="cap">Dunmore Construction<br>Lorem ipsum dolor sit amet, consectetur</div></div>
    <div class="work" style="left:104px;top:118px"><div style="height:100%;background:linear-gradient(135deg,#1d2a6a,#8a7a6a)" role="img" aria-label="Community website"></div><div class="cap">Orchard Hill<br>Lorem ipsum dolor sit amet, consectetur</div></div>
    <div class="work" style="left:187px;top:118px"><div style="height:100%;background:linear-gradient(180deg,#f2f2f2 40%,#4a3a30)" role="img" aria-label="Interior design website"></div><div class="cap">Tessaline<br>Lorem ipsum dolor sit amet, consectetur</div></div>
    <div class="work" style="left:24px;top:183px"><div style="height:100%;background:linear-gradient(135deg,#3f6fb8,#a9b4c4)" role="img" aria-label="Car rental website"></div><div class="cap">Sunward Drive<br>Lorem ipsum dolor sit amet, consectetur</div></div>
    <div class="work" style="left:104px;top:183px"><div style="height:100%;background:linear-gradient(135deg,#e9d9cf,#b98a6a)" role="img" aria-label="Personal coaching website"></div><div class="cap">Mira Calder<br>Lorem ipsum dolor sit amet, consectetur</div></div>
    <div class="work" style="left:187px;top:183px"><div style="height:100%;background:linear-gradient(135deg,#1b2a8a,#8a2a3a)" role="img" aria-label="Volunteer team website"></div><div class="cap">Team Rescue North<br>Lorem ipsum dolor sit amet, consectetur</div></div>
    <div class="abs btn">See more</div>
  </section>

  <section class="abs quote">
    <div class="abs serif" style="left:140px;top:6px;font-size:14px;color:#777">&ldquo;</div>
    <div class="abs" style="left:36px;top:26px;width:30px;height:30px;border-radius:50%;background:linear-gradient(160deg,#d9cbb8,#6d5a4a)" role="img" aria-label="Client portrait"></div>
    <p class="abs">"Lorem ipsum dolor sit amet, consectetur adipiscing elit. Fusce iaculis, lorem a vulputate euismod, felis erat scelerisque eros, a convallis eros enim ac nibh. Duis luctus bibendum mauris, sit amet vehicula mi.</p>
    <div class="abs" style="left:76px;top:54px;font-size:3.2px;color:#888;font-style:italic">- Martin Vale, President of the Vale Group and Author of Five Lessons for a Team</div>
    <svg class="abs" style="left:2px;top:34px" width="8" height="12"><rect width="8" height="12" fill="#444"/><path d="M5 3L3 6l2 3" fill="none" stroke="#ddd" stroke-width=".8"/></svg>
    <svg class="abs" style="left:282px;top:34px" width="8" height="12"><rect width="8" height="12" fill="#444"/><path d="M3 3l2 3-2 3" fill="none" stroke="#ddd" stroke-width=".8"/></svg>
  </section>

  <section class="abs team">
    <div class="abs serif sec-title" style="top:9px">Our Team</div>
    <div class="member" style="left:30px;top:38px"><div class="photo" role="img" aria-label="Team member portrait"></div><h4>Owen Tallis</h4><p>"Morbi gravida, ante at laoreet accumsan, justo tellus feugiat sem, vel sollicitudin enim lorem vitae arcu. Sed vel nulla ultricies sem sodales finibus."</p></div>
    <div class="member" style="left:150px;top:38px"><div class="photo" role="img" aria-label="Team member portrait"></div><h4>Nadia Ferris</h4><p>"Morbi gravida, ante at laoreet accumsan, justo tellus feugiat sem, vel sollicitudin enim lorem vitae arcu. Sed vel nulla ultricies sem sodales finibus."</p></div>
    <div class="member" style="left:30px;top:80px"><div class="photo" role="img" aria-label="Team member portrait"></div><h4>Elliot Crane</h4><p>"Morbi gravida, ante at laoreet accumsan, justo tellus feugiat sem, vel sollicitudin enim lorem vitae arcu. Sed vel nulla ultricies sem sodales finibus."</p></div>
    <div class="member" style="left:150px;top:80px"><div class="photo" role="img" aria-label="Team member portrait"></div><h4>Priya Holm</h4><p>"Morbi gravida, ante at laoreet accumsan, justo tellus feugiat sem, vel sollicitudin enim lorem vitae arcu. Sed vel nulla ultricies sem sodales finibus."</p></div>
  </section>

  <section class="abs contact">
    <div class="abs serif" style="left:24px;top:27px;font-size:12.5px;line-height:16px">Get a free audit<br>and consultation</div>
    <svg class="abs" style="left:34px;top:67px" width="8" height="8" viewBox="0 0 24 24"><path d="M6.6 10.8a15 15 0 006.6 6.6l2.2-2.2a1 1 0 011-.25 11 11 0 003.6.6 1 1 0 011 1V20a1 1 0 01-1 1A17 17 0 013 4a1 1 0 011-1h3.5a1 1 0 011 1 11 11 0 00.6 3.6 1 1 0 01-.25 1z" fill="#fff"/></svg>
    <div class="abs" style="left:48px;top:67px;font-size:6.5px">555-010-4821</div>
    <svg class="abs" style="left:34px;top:85px" width="8" height="6"><rect width="8" height="6" fill="#fff"/><path d="M0 0l4 3.5L8 0" fill="none" stroke="#262626" stroke-width=".8"/></svg>
    <div class="abs" style="left:48px;top:84px;font-size:6.5px">hello@kestran.example</div>
  </section>
  <section class="abs form">
    <div class="field-label" style="left:11px;top:16px">First Name *</div><div class="field" style="left:11px;top:20px;width:109px;height:8px"></div>
    <div class="field-label" style="left:11px;top:35px">Email Address</div><div class="field" style="left:11px;top:39px;width:109px;height:8px"></div>
    <div class="field-label" style="left:11px;top:54px">Phone Number</div><div class="field" style="left:11px;top:58px;width:109px;height:8px"></div>
    <div class="field-label" style="left:11px;top:73px">Message</div><div class="field" style="left:11px;top:77px;width:109px;height:29px"></div>
    <div class="abs btn" style="left:11px;top:117px;width:58px;height:9px;font-size:2.6px">Submit</div>
  </section>

  <footer class="abs footer">
    <div class="abs brand" style="left:26px;top:15px;font-size:11px;color:#fff">KESTRAN<small>STRATEGIES</small></div>
    <svg class="abs" style="left:204px;top:15px" width="56" height="10"><g fill="none" stroke="#fff" stroke-width="1"><circle cx="5" cy="5" r="4.2"/><circle cx="21" cy="5" r="4.2"/><circle cx="37" cy="5" r="4.2"/><circle cx="52" cy="5" r="3.5"/></g></svg>
    <div class="abs" style="left:24px;top:45px;font-size:3.4px;color:#bbb">&copy;2021 KESTRAN STRATEGIES. All rights reserved.</div>
  </footer>
</div>

<!-- ================= full-size homepage ================= -->
<div class="abs full">

  <section class="abs hero">
    <div class="abs video shot" role="img" aria-label="Laptop with code editor on a desk"></div>
    <svg class="abs" style="left:412px;top:195px" width="44" height="44" viewBox="0 0 44 44"><circle cx="22" cy="22" r="20" fill="none" stroke="rgba(255,255,255,.5)" stroke-width="2.5"/><path d="M17 13l14 9-14 9z" fill="rgba(255,255,255,.5)"/></svg>
    <div class="abs navbar"></div>
    <div class="abs brand" style="left:53px;top:37px;font-size:21px">KESTRAN<small>STRATEGIES</small></div>
    <nav class="abs navlinks">
      <span style="left:0">Home</span><span style="left:50px">What We Do</span><span style="left:135px">Portfolio</span><span style="left:202px">Testimonials</span><span style="left:286px">Our Team</span><span style="left:354px">Contact</span>
    </nav>
    <h1 class="abs serif">We Build<br>Value</h1>
    <p class="abs lead">Enterprise Level<br>Website Development<br>and Online Marketing</p>
    <div class="abs btn">See how we do it</div>
  </section>

  <section class="abs services">
    <svg class="abs" style="left:288px;top:31px" width="316" height="369"><path d="M4 31V4H311V364H230" fill="none" stroke="var(--gold)" stroke-width="8"/></svg>
    <div class="abs kicker" style="left:52px;top:42px">What we do</div>
    <div class="abs serif svc-title" style="left:52px;top:65px">These are the things we CRUSH</div>
    <div class="card" style="left:134px;top:117px"><div class="art" style="background:linear-gradient(160deg,#3b6fd0,#d9dde6)" role="img" aria-label="Website screenshots"></div><div class="label">Websites</div></div>
    <div class="card" style="left:262px;top:117px"><div class="art" style="background:linear-gradient(160deg,#6c9fd6,#e0c58a)" role="img" aria-label="Landing page screenshots"></div><div class="label">Landing Pages</div></div>
    <div class="card" style="left:393px;top:117px"><div class="art" style="background:linear-gradient(160deg,#4b2a1c,#a0552c)" role="img" aria-label="Donation page screenshot"></div><div class="label">Donation Pages</div></div>
    <div class="card" style="left:135px;top:309px"><div class="art" style="background:linear-gradient(160deg,#3a1f7a,#7a3fb5)" role="img" aria-label="Sales funnel illustration"></div><div class="label">PPC and Funnels</div></div>
    <div class="card" style="left:263px;top:309px"><div class="art" style="background:linear-gradient(160deg,#c9c23a,#3b3a6e)" role="img" aria-label="Video marketing laptop illustration"></div><div class="label">Video Marketing</div></div>
    <div class="card" style="left:393px;top:309px"><div class="art" style="background:linear-gradient(160deg,#5ec0bd,#3d8f8c)" role="img" aria-label="Analytics magnifier illustration"></div><div class="label">Analytics and<br>Optimization</div></div>
  </section>

  <section class="abs portfolio">
    <div class="abs serif sec-title" style="top:38px">Our Portfolio</div>
    <div class="work" style="left:52px;top:115px"><div class="shot" style="height:100%" role="img" aria-label="Production company website"></div><div class="cap"><b>Marlow Productions</b>Lorem ipsum dolor sit amet, consectetur</div></div>
    <div class="work" style="left:235px;top:115px"><div style="height:100%;background:linear-gradient(135deg,#5d4a8c,#c9b7a8)" role="img" aria-label="Charity website"></div><div class="cap"><b>Hearthside Care</b>Lorem ipsum dolor sit amet, consectetur</div></div>
    <div class="work" style="left:419px;top:115px"><div style="height:100%;background:linear-gradient(135deg,#2b3340,#7b8392)" role="img" aria-label="Fitness website"></div><div class="cap"><b>Ferrit X</b>Lorem ipsum dolor sit amet, consectetur</div></div>
  </section>
</div>

</body>
</html>
```